Talvex Engineering Business card Design

We need to make business cards for our NDT and inspection company. The company is called Talvex Engineering. We want a professional modern feel business card. We have just completed the remaking of our website and would like to have business cards with the same feel and colours. The final design should communicate professionalism and cutting edge tech.

Target Market(s)

We sell to B2B Business clients. Our customer is an engineer or decision maker in the mechanical engineering / Oil and gas field.

Contact Information for Business Card

Please see the current business cards that we have uploaded to get the details. You can also look at our Website www.talvex-eng.example for more.

Requirements
Must have
• Less is more
Nice to have
• Less is more

```html
<!DOCTYPE html>
<html lang="en">
<head>
<meta charset="utf-8">
<title>Talvex Engineering – Business Card</title>
<link rel="stylesheet" href="https://fonts.googleapis.com/css2?family=Roboto:wght@400;500;700&family=Roboto+Condensed:wght@700&display=swap">
<style>
  :root {
    --navy: #1f2f6b;
    --red: #b3141c;
    --grey-text: #555a63;
    --card: #fbfbfa;
    --backdrop: #c9c9c9;
  }
  * { box-sizing: border-box; margin: 0; padding: 0; }
  html, body { width: 1200px; height: 852px; overflow: hidden; }
  body {
    background: var(--backdrop);
    font-family: "Roboto", Arial, sans-serif;
    position: relative;
  }
  .card {
    position: absolute;
    width: 560px;
    height: 320px;
    background: var(--card);
    border-radius: 14px;
    overflow: hidden;
    box-shadow: 0 4px 12px rgba(0,0,0,.18);
  }
  /* Services side */
  .card--services { left: 90px; top: 100px; }
  .brand-mark {
    position: absolute;
    top: 44px; left: 0; right: 0;
    display: flex; align-items: center; justify-content: center; gap: 12px;
  }
  .brand-mark__dot {
    width: 26px; height: 26px; border-radius: 50%;
    background: var(--navy);
  }
  .brand-mark__name {
    font-weight: 700; font-size: 26px; color: var(--navy); letter-spacing: .2px;
  }
  .services {
    position: absolute;
    top: 122px; left: 0; right: 0;
    text-align: center;
    font-size: 11.5px;
    line-height: 17px;
  }
  .services__line--primary { color: var(--navy); }
  .services__line--accent { color: var(--red); }
  .services__line--muted { color: var(--grey-text); }
  .band {
    position: absolute; left: 0; right: 0; top: 232px; height: 10px;
    display: flex;
  }
  .band__red { flex: 0 0 40%; background: var(--red); }
  .band__navy { flex: 1; background: var(--navy); }
  .edge-strip {
    position: absolute; left: 0; right: 0; bottom: 0; height: 8px;
    background: var(--red);
  }
  /* Contact side */
  .card--contact { left: 550px; top: 440px; }
  .card__swoosh { position: absolute; inset: 0; }
  .holder {
    position: absolute; right: 24px; top: 16px; text-align: right; color: #fff;
  }
  .holder__name {
    font-family: "Roboto Condensed", "Roboto", sans-serif;
    font-weight: 700; font-size: 21px;
  }
  .holder__title { font-size: 13px; margin-top: 2px; }
  .contact-brand {
    position: absolute; left: 34px; top: 212px;
    display: flex; align-items: center; gap: 10px;
  }
  .contact-brand__dot {
    width: 22px; height: 22px; border-radius: 50%; background: var(--navy);
  }
  .contact-brand__name {
    font-weight: 700; font-size: 20px; color: var(--navy);
  }
  .contact {
    position: absolute; right: 22px; top: 150px;
    color: var(--navy); font-size: 13px; line-height: 18px; text-align: right;
  }
  .contact__address { margin-bottom: 16px; }
  .contact__row { display: flex; align-items: center; justify-content: flex-end; gap: 8px; }
  .contact__icon { width: 12px; height: 12px; flex: 0 0 12px; }
</style>
</head>
<body>

  <section class="card card--services" aria-label="Card back – services">
    <div class="brand-mark">
      <span class="brand-mark__dot"></span>
      <span class="brand-mark__name">Talvex Engineering</span>
    </div>
    <div class="services">
      <p class="services__line--primary">API 653 Tank Inspections | API 570 Pipeline Inspections | API 510 Pressure</p>
      <p class="services__line--primary">Vessel Inspections | Welding Inspection | Electrical Inspection</p>
      <p class="services__line--accent">OCTG Inspections | Lifting Equipment Inspections</p>
      <p class="services__line--accent">Non-Destructive Testing | UT/PT/MT/RT/VT | Advanced NDT | PAUT/MFL/ILI</p>
      <p class="services__line--muted">Engineering Projects</p>
    </div>
    <div class="band"><span class="band__red"></span><span class="band__navy"></span></div>
    <div class="edge-strip"></div>
  </section>

  <section class="card card--contact" aria-label="Card front – contact">
    <svg class="card__swoosh" viewBox="0 0 560 320" aria-hidden="true">
      <path fill="var(--navy)" d="M0,0 H560 V62 C440,70 320,86 220,112 C140,134 70,158 0,180 Z"/>
      <path fill="none" stroke="var(--red)" stroke-width="7" d="M0,196 C80,166 150,142 230,122 C340,96 450,80 560,72"/>
      <path fill="none" stroke="var(--red)" stroke-width="3" d="M20,214 C90,184 170,158 260,138"/>
    </svg>
    <div class="holder">
      <p class="holder__name">Daniel Kimaro</p>
      <p class="holder__title">Environmental Manager</p>
    </div>
    <div class="contact-brand">
      <span class="contact-brand__dot"></span>
      <span class="contact-brand__name">Talvex Engineering</span>
    </div>
    <div class="contact">
      <p class="contact__address">P.O. BOX 40512-80100<br>Mombasa Kenya</p>
      <p class="contact__row">+ 254 20 555 0142/3
        <svg class="contact__icon" viewBox="0 0 12 12" aria-hidden="true"><path fill="var(--red)" d="M2 1h2l1 3-1.5 1a7 7 0 0 0 3.5 3.5L8 7l3 1v2a1 1 0 0 1-1 1A9 9 0 0 1 1 2a1 1 0 0 1 1-1z"/></svg>
      </p>
      <p class="contact__row">info@talvex-eng.example
        <svg class="contact__icon" viewBox="0 0 12 12" aria-hidden="true"><rect x="0.5" y="2.5" width="11" height="7" fill="var(--red)"/><path d="M1 3l5 4 5-4" fill="none" stroke="#fff" stroke-width="1"/></svg>
      </p>
      <p class="contact__row">www.talvex-eng.example
        <svg class="contact__icon" viewBox="0 0 12 12" aria-hidden="true"><circle cx="6" cy="6" r="5.5" fill="var(--red)"/><path d="M0.5 6h11M6 0.5c-2.5 3-2.5 8 0 11M6 0.5c2.5 3 2.5 8 0 11" fill="none" stroke="#fff" stroke-width=".8"/></svg>
      </p>
    </div>
  </section>

</body>
</html>
```